Webdesign für Hundeerziehungsberatung
Zielgruppe:
Hundehalter, die entweder einen Welpen angeschafft haben, ihren Hund ausbilden oder fördern wollen sowie Menschen mit einem 'Problemhund'.
Die Hundeerziehungsberatung bietet Hundehaltern die Erziehung im Einzelsetting und im Gruppensetting an.
Aufgabenstellung
die Farben sollen sich am Logo orientieren, gern noch eine Farbe dazu. Logo anbei, Bilder anbei. Flyer anbei
Sollten die Bilder ausreichen bitten wir um Auswahl bei pixel.morvani. Tool: Photoshop.
Der Kundin gefällt: https://www.pfotenlauf-brevik.de/

```html
<!DOCTYPE html>
<html lang="de">
<head>
<meta charset="utf-8">
<title>Pfotenweg – Hundeerziehungsberatung</title>
<link href="https://fonts.googleapis.com/css2?family=Roboto:wght@400;500;700&display=swap" rel="stylesheet">
<style>
:root{
  --orange:#dc8f48;
  --text:#3f3f3f;
  --muted:#7a6e66;
  --light:#f6f6f6;
  --band:#e1e1e1;
  --footer:#3a3a3a;
  --white:#fff;
  --line:#c9c9c9;
}
*{box-sizing:border-box;margin:0;padding:0}
html,body{width:1200px;height:3145px;overflow:hidden}
body{font-family:'Roboto',sans-serif;color:var(--text);background:var(--light);position:relative}
.btn{display:inline-flex;align-items:center;justify-content:center;height:30px;min-width:158px;padding:0 14px;background:var(--orange);color:#fff;font-size:12.5px;text-transform:uppercase;letter-spacing:.2px;text-decoration:none}
.btn-outline{background:#fff;color:var(--orange);border:1px solid var(--orange)}
.topbar{position:absolute;top:0;left:0;width:1200px;height:27px;background:var(--orange);color:#fff;font-size:12.5px;display:flex;justify-content:flex-end;align-items:center;gap:26px;padding-right:44px}
.topbar span{display:flex;align-items:center;gap:8px}
.nav{position:absolute;top:27px;left:0;width:1200px;height:64px;background:#fff;display:flex;align-items:center;justify-content:space-between;padding:0 44px 0 34px;box-shadow:0 1px 4px rgba(0,0,0,.1);z-index:2}
.brand{display:flex;align-items:center;gap:8px;font-size:19px;color:#8a7d74}
.brand i{width:30px;height:30px;border:2px solid #8a7d74;border-radius:50%}
.nav ul{list-style:none;display:flex;gap:21px;font-size:12.5px;text-transform:uppercase;color:var(--text)}
.hero{position:absolute;top:91px;left:0;width:1200px;height:442px;background:linear-gradient(100deg,#c7a06b 0%,#d6b17e 35%,#9a9a98 60%,#c89a5a 85%,#b58a55 100%)}
.hero-box{position:absolute;left:34px;top:81px;width:325px;height:271px;background:rgba(255,255,255,.88);padding:18px 22px}
.hero-box h1{color:var(--orange);font-size:32px;line-height:41px;font-weight:700}
.hero-box h2{color:var(--muted);font-size:20px;font-weight:400;margin:4px 0 12px}
.hero-box p{font-size:12.5px;line-height:20px;margin-bottom:24px}
.hero-box .actions{display:flex;gap:10px}
.hero-box .btn{min-width:119px}
.hero-box .btn-outline{min-width:148px}
.section-title{color:var(--orange);font-size:31px;font-weight:700}
.subline{color:var(--muted);font-size:20px;margin-top:14px}
.services{position:absolute;top:533px;left:0;width:1200px;height:624px;padding:70px 59px 0}
.cards{position:absolute;left:59px;display:flex;gap:54px}
.card{width:325px;background:#fff;box-shadow:0 1px 6px rgba(0,0,0,.15);padding:21px}
.card .photo{height:155px;background:linear-gradient(135deg,#8c8c88,#6b5a4c 60%,#3a3330)}
.card .photo.grass{background:linear-gradient(135deg,#3c5a2a,#7aa048 60%,#2e2f2c)}
.card h3{color:var(--orange);font-size:19px;font-weight:500;margin:20px 0 9px}
.card p{font-size:12.5px;line-height:20px}
.card .btn{margin-top:18px}
.services .cards{top:164px}
.services .card{height:357px}
.company{position:absolute;top:1157px;left:0;width:1200px;height:309px;background:var(--band);padding:38px 59px}
.company h2{font-size:31px;font-weight:500;color:var(--text);margin-bottom:18px}
.company p{width:425px;font-size:12.5px;line-height:20px;margin-bottom:24px}
.events{position:absolute;top:1466px;left:0;width:1200px;height:744px;padding:104px 59px 0}
.events .cards{top:199px}
.events .card{height:437px}
.events .meta{font-size:12.5px;line-height:20px;padding-bottom:10px;border-bottom:1px solid var(--line);margin-bottom:10px}
.schedule{position:absolute;top:2210px;left:0;width:1200px;height:775px;background:var(--band)}
.schedule-intro{position:absolute;left:59px;top:42px;width:260px}
.schedule-intro h2{font-size:31px;font-weight:500;line-height:42px}
.schedule-intro .subline{margin:12px 0 24px}
.schedule-intro p{font-size:12.5px;line-height:20px;margin-bottom:20px}
.timetable{position:absolute;left:441px;top:40px;width:698px;height:680px;background:#fff;border-radius:4px;padding:22px 29px}
.timetable table{width:640px;border-collapse:collapse;font-size:14px}
.timetable th{text-align:left;color:var(--orange);font-size:20px;font-weight:500;height:40px;border-bottom:1px solid var(--line);padding-left:12px}
.timetable td{vertical-align:top;padding:22px 0 0 12px;border-bottom:1px solid var(--line);line-height:37px}
.timetable td.day{font-weight:500;line-height:37px}
.timetable tr.two td{height:105px}
.timetable tr.one td{height:75px}
.timetable tr:last-child td{border-bottom:none}
.footer{position:absolute;top:2985px;left:0;width:1200px;height:160px;background:var(--footer);color:#fff}
.footer .brand{position:absolute;left:68px;top:52px;color:#fff}
.footer .brand i{border-color:#fff}
.footer .col{position:absolute;top:47px;font-size:12.5px;line-height:26px}
.footer h4{font-size:15px;font-weight:700;margin-bottom:2px}
.footer .col span{display:flex;align-items:center;gap:10px}
.footer .legal{font-size:11px;line-height:21px}
</style>
</head>
<body>
<header>
  <div class="topbar">
    <span><svg width="13" height="13" viewBox="0 0 24 24"><path fill="#fff" d="M6.6 10.8a15.1 15.1 0 006.6 6.6l2.2-2.2a1 1 0 011-.25 11.4 11.4 0 003.6.6 1 1 0 011 1V20a1 1 0 01-1 1A17 17 0 013 4a1 1 0 011-1h3.5a1 1 0 011 1c0 1.25.2 2.45.57 3.57a1 1 0 01-.25 1z"/></svg>+ 04471-3069215</span>
    <span><svg width="14" height="11" viewBox="0 0 24 18"><path fill="#fff" d="M2 0h20a2 2 0 012 2v14a2 2 0 01-2 2H2a2 2 0 01-2-2V2a2 2 0 012-2zm10 8L22 2H2z"/></svg>kontakt@pfotenweg-beratung.de</span>
  </div>
  <nav class="nav">
    <div class="brand"><i></i>Pfotenweg</div>
    <ul><li>Home</li><li>Trainingsangebote</li><li>Unternehmen</li><li>Veranstaltungen</li><li>Kurse</li><li>Kontakt</li></ul>
  </nav>
</header>

<section class="hero" role="img" aria-label="Foto: Trainerin im Freien sitzt einer schwarz-weißen Bulldogge gegenüber, herbstliches Gras im Hintergrund">
  <div class="hero-box">
    <h1>HundMenschen Beziehung</h1>
    <h2>Hundeerziehungsberatung</h2>
    <p>Lorem ipsum dolor sit amet, consectetuer adipiscing elit. Aenean commodo ligula eget dolor. Aenean massa. Cum sociis natoque penatibus et</p>
    <div class="actions"><a class="btn">Einzeltraining</a><a class="btn btn-outline">Gruppentraining</a></div>
  </div>
</section>

<section class="services">
  <h2 class="section-title">Meine Leistungen für Sie</h2>
  <div class="subline">Subline</div>
  <div class="cards">
    <article class="card"><div class="photo" role="img" aria-label="Foto: Hundepfoten auf einer Fußmatte"></div><h3>Erstgespräche</h3><p>Lorem ipsum dolor sit amet, consectetuer adipiscing elit. Aenean commodo ligula eget dolor. Aenean massa. Cum sociis natoque</p><a class="btn">Termin vereinbaren</a></article>
    <article class="card"><div class="photo grass" role="img" aria-label="Foto: Hund liegt im Gras"></div><h3>Erziehung im Einzelsetting</h3><p>Lorem ipsum dolor sit amet, consectetuer adipiscing elit. Aenean commodo ligula eget dolor. Aenean massa. Cum sociis natoque</p><a class="btn">Termin vereinbaren</a></article>
    <article class="card"><div class="photo grass" role="img" aria-label="Foto: mehrere Hunde spielen auf einer Wiese"></div><h3>Erziehung im Gruppensetting</h3><p>Lorem ipsum dolor sit amet, consectetuer adipiscing elit. Aenean commodo ligula eget dolor. Aenean massa. Cum sociis natoque</p><a class="btn">Kurs finden</a></article>
  </div>
</section>

<section class="company">
  <h2>Unternehmen</h2>
  <p>Lorem ipsum dolor sit amet, consectetuer adipiscing elit. Aenean commodo ligula eget dolor. Aenean massa. Cum sociis natoque penatibus et magnis dis parturient montes, nascetur ridiculus mus nascetur ridiculus .Lorem ipsum dolor sit amet, consectetuer adipiscing elit. Aenean commodo ligula eget dolor. Aenean massa. Cum sociis natoque penatibus et magnis dis parturient montes, nascetur ridiculus mus nascetur ridiculus .</p>
  <a class="btn">Erstgespräch vereinbaren</a>
</section>

<section class="events">
  <h2 class="section-title">Bevorstehende Veranstaltungen</h2>
  <div class="subline">Subline</div>
  <div class="cards">
    <article class="card"><div class="photo" role="img" aria-label="Foto: Hundepfoten auf einer Fußmatte"></div><h3>Lorem ipsum dolor</h3><div class="meta"><b>Was?</b> 2 x Praxistage<br><b>Wann?</b> Samstag - Sonntag 21.-23.08.2020<br><b>Wo?</b> Köln</div><p>Lorem ipsum dolor sit amet, consectetuer adipiscing elit. Aenean commodo ligula eget dolor. Aenean massa. Cum sociis natoque</p><a class="btn">Mehr erfahren</a></article>
    <article class="card"><div class="photo" role="img" aria-label="Foto: Hundepfoten auf einer Fußmatte"></div><h3>Lorem ipsum dolor</h3><div class="meta"><b>Was?</b> 2 x Praxistage<br><b>Wann?</b> Samstag - Sonntag 21.-23.08.2020<br><b>Wo?</b> Köln</div><p>Lorem ipsum dolor sit amet, consectetuer adipiscing elit. Aenean commodo ligula eget dolor. Aenean massa. Cum sociis natoque</p><a class="btn">Mehr erfahren</a></article>
    <article class="card"><div class="photo" role="img" aria-label="Foto: Hundepfoten auf einer Fußmatte"></div><h3>Lorem ipsum dolor</h3><div class="meta"><b>Was?</b> 2 x Praxistage<br><b>Wann?</b> Samstag - Sonntag 21.-23.08.2020<br><b>Wo?</b> Köln</div><p>Lorem ipsum dolor sit amet, consectetuer adipiscing elit. Aenean commodo ligula eget dolor. Aenean massa. Cum sociis natoque</p><a class="btn">Mehr erfahren</a></article>
  </div>
</section>

<section class="schedule">
  <div class="schedule-intro">
    <h2>Erziehung<br>im Gruppensetting</h2>
    <div class="subline">Termine</div>
    <p>Lorem ipsum dolor sit amet, consectetuer adipiscing elit. Aenean commodo ligula eget dolor. Aenean massa. Cum sociis natoque penatibus et magnis dis parturient montes, nascetur ridiculus mus nascetur ridiculus .</p>
    <a class="btn">Kurs buchen</a>
  </div>
  <div class="timetable">
    <table>
      <colgroup><col style="width:144px"><col style="width:132px"><col></colgroup>
      <thead><tr><th>Wochentag</th><th>Uhrzeit</th><th>Gruppe</th></tr></thead>
      <tbody>
        <tr class="two"><td class="day">Montag</td><td>12:00 -13:00<br>14:00 -15:00</td><td>Welpen – „Von Anfang an“<br>Kontakte – „Gemeinsam und miteinander“</td></tr>
        <tr class="two"><td class="day">Dienstag</td><td>12:00 -13:00<br>14:00 -15:00</td><td>Welpen – „Von Anfang an“<br>Kontakte – „Gemeinsam und miteinander“</td></tr>
        <tr class="one"><td class="day">Mittwoch</td><td>-</td><td>-</td></tr>
        <tr class="one"><td class="day">Donnerstag</td><td>14:00 -15:00</td><td>Kontakte – „Gemeinsam und miteinander“</td></tr>
        <tr class="one"><td class="day">Freitag</td><td>14:00 -15:00</td><td>Kontakte – „Gemeinsam und miteinander“</td></tr>
        <tr class="two"><td class="day">Samstag</td><td>12:00 -13:00<br>14:00 -15:00</td><td>Welpen – „Von Anfang an“<br>Kontakte – „Gemeinsam und miteinander“</td></tr>
        <tr class="one"><td class="day">Sonntag</td><td>-</td><td>-</td></tr>
      </tbody>
    </table>
  </div>
</section>

<footer class="footer">
  <div class="brand"><i></i>Pfotenweg</div>
  <div class="col" style="left:267px">
    <h4>Kontakt</h4>
    <span><svg width="13" height="13" viewBox="0 0 24 24"><path fill="#fff" d="M6.6 10.8a15.1 15.1 0 006.6 6.6l2.2-2.2a1 1 0 011-.25 11.4 11.4 0 003.6.6 1 1 0 011 1V20a1 1 0 01-1 1A17 17 0 013 4a1 1 0 011-1h3.5a1 1 0 011 1c0 1.25.2 2.45.57 3.57a1 1 0 01-.25 1z"/></svg>+ 04471-3069215</span>
    <span><svg width="14" height="11" viewBox="0 0 24 18"><path fill="#fff" d="M2 0h20a2 2 0 012 2v14a2 2 0 01-2 2H2a2 2 0 01-2-2V2a2 2 0 012-2zm10 8L22 2H2z"/></svg>kontakt@pfotenweg-beratung.de</span>
  </div>
  <div class="col" style="left:477px">
    <h4>Rechtliches</h4>
    <div class="legal">Impressum<br>Datenschutz</div>
  </div>
</footer>
</body>
</html>
```